Client questionnaire

Quillon Ravenmoor Group (www.quillonravenmoor.com.au) needs a document designed to bring out as a questionnaire to speak with potential clients. Sales staff and planners will use this in introductions to ask basic questions but to also scribble notes and draw pictures on top of the graph.
I've attached two files which are the content that we wish to include.
1. Financial life cycle: this has two pages. Please design it so that the financial snap shot is on a different page than the lifecycle and graph. I will leave it to the designer to decide whether landscape or portrait is best - please ensure though that they are both landscape or both portrait on this document as they will be printed back to back on the same sheet.
2. Goals diagram - please theme this in the same way as the above document.
3. I've attached the logo to be used too - filename: QuillonRavenmoorgroup.eps

Group

```html
<!DOCTYPE html>
<html lang="en">
<head>
<meta charset="utf-8">
<title>Questionnaire – Quillon Ravenmoor Group</title>
<link href="https://fonts.googleapis.com/css2?family=Open+Sans:wght@300;400;600;700&display=swap" rel="stylesheet">
<style>
  :root {
    --brand-blue: #1f82b8;
    --ink: #1a1a1a;
    --rule: #9a9a9a;
    --box-line: #222;
    --phase-1: #00aaea;
    --phase-2: #0292e6;
    --phase-3: #0866e6;
    --white: #ffffff;
    --paper: #ffffff;
  }
  * { box-sizing: border-box; margin: 0; padding: 0; }
  html, body { width: 848px; height: 1200px; overflow: hidden; background: var(--paper); }
  body { position: relative; font-family: "Open Sans", Verdana, sans-serif; color: var(--ink); }

  .masthead {
    position: absolute; left: 51px; top: 43px; width: 742px; height: 113px;
    background: var(--brand-blue); color: var(--white);
  }
  .brand {
    position: absolute; left: 40px; top: 10px; width: 112px;
    display: flex; flex-direction: column; align-items: center; gap: 6px;
  }
  .brand-mark { width: 54px; height: 54px; border: 2px solid var(--white); border-radius: 50%; }
  .brand-name {
    font-size: 10.5px; font-weight: 400; letter-spacing: 0.5px; line-height: 1.2;
    text-transform: uppercase; text-align: center; color: var(--white);
  }
  .masthead-title {
    position: absolute; left: 246px; top: 22px;
    font-size: 27px; font-weight: 300; letter-spacing: 3px;
  }

  .answer-head { position: absolute; top: 170px; font-size: 14px; }
  .answer-head.yes { left: 352px; }
  .answer-head.no { left: 396px; }
  .answer-head.remarks { left: 577px; }

  .question {
    position: absolute; left: 97px; width: 240px;
    font-size: 13.5px; line-height: 1.3;
  }
  .leader { position: absolute; height: 1px; background: var(--rule); }
  .tick-circle {
    position: absolute; width: 28px; height: 28px;
    border: 1.3px solid var(--box-line); border-radius: 50%; background: var(--paper);
  }
  .remarks-box {
    position: absolute; left: 433px; top: 197px; width: 342px; height: 291px;
    border: 1.3px solid var(--box-line);
    display: grid; grid-template-rows: repeat(6, 1fr);
  }
  .remarks-row { border-bottom: 1.3px solid var(--box-line); }
  .remarks-row:last-child { border-bottom: none; }

  .growth-chart { position: absolute; left: 100px; top: 500px; width: 620px; height: 275px; }

  .phase-table {
    position: absolute; left: 141px; top: 783px; width: 597px; height: 344px;
    border: 1.3px solid var(--box-line);
    display: grid; grid-template-columns: repeat(3, 1fr);
    grid-template-rows: 58px 167px 1fr;
    text-align: center; font-size: 12.5px; line-height: 1.3;
  }
  .cell {
    border-right: 1.3px solid var(--box-line);
    display: flex; flex-direction: column; justify-content: center; align-items: center;
    padding: 4px 8px;
  }
  .cell:nth-child(3n) { border-right: none; }
  .cell.head, .cell.situation { border-bottom: 1.5px dotted var(--box-line); }
  .phase-number { font-size: 12px; }
  .phase-name { font-size: 15px; font-weight: 700; line-height: 1.2; text-transform: uppercase; }
  .cell-title { font-weight: 700; text-decoration: underline; }
  .cell ul { list-style: none; }
  .cell li::before { content: "• "; }
</style>
</head>
<body>

<header class="masthead">
  <div class="brand">
    <span class="brand-mark"></span>
    <span class="brand-name">Quillon Ravenmoor Group</span>
  </div>
  <h1 class="masthead-title">QUESTIONNAIRE</h1>
</header>

<span class="answer-head yes">Yes</span>
<span class="answer-head no">No</span>
<span class="answer-head remarks">Remarks</span>

<p class="question" style="top:203px">Do you keep track of where all your money is spent?</p>
<p class="question" style="top:259px">Do you do your own tax return?</p>
<p class="question" style="top:298px">Do you have a preferred investment type (Shares, property, other)?</p>
<p class="question" style="top:355px">Do you have multiple super funds?</p>
<p class="question" style="top:405px">Do you have a home loan?</p>
<p class="question" style="top:442px">Do you have enough savings to fund your lifestyle if you couldn’t work?</p>

<span class="leader" style="left:296px;top:220px;width:56px"></span>
<span class="leader" style="left:306px;top:269px;width:46px"></span>
<span class="leader" style="left:326px;top:318px;width:26px"></span>
<span class="leader" style="left:306px;top:365px;width:46px"></span>
<span class="leader" style="left:276px;top:415px;width:76px"></span>
<span class="leader" style="left:330px;top:463px;width:22px"></span>

<span class="tick-circle" style="left:350px;top:206px"></span><span class="tick-circle" style="left:390px;top:206px"></span>
<span class="tick-circle" style="left:350px;top:255px"></span><span class="tick-circle" style="left:390px;top:255px"></span>
<span class="tick-circle" style="left:350px;top:304px"></span><span class="tick-circle" style="left:390px;top:304px"></span>
<span class="tick-circle" style="left:350px;top:351px"></span><span class="tick-circle" style="left:390px;top:351px"></span>
<span class="tick-circle" style="left:350px;top:401px"></span><span class="tick-circle" style="left:390px;top:401px"></span>
<span class="tick-circle" style="left:350px;top:449px"></span><span class="tick-circle" style="left:390px;top:449px"></span>

<div class="remarks-box">
  <div class="remarks-row"></div><div class="remarks-row"></div><div class="remarks-row"></div>
  <div class="remarks-row"></div><div class="remarks-row"></div><div class="remarks-row"></div>
</div>

<svg class="growth-chart" viewBox="100 500 620 275" aria-label="Wealth growth across three phases">
  <rect x="143" y="505" width="186" height="264" fill="var(--phase-1)"/>
  <rect x="329" y="505" width="188" height="264" fill="var(--phase-2)"/>
  <rect x="517" y="505" width="189" height="264" fill="var(--phase-3)"/>
  <line x1="144" y1="505" x2="144" y2="770" stroke="#111" stroke-width="4"/>
  <line x1="142" y1="769" x2="706" y2="769" stroke="#111" stroke-width="4"/>
  <polyline points="144,761 329,715 517,641 706,524" fill="none" stroke="#111" stroke-width="1.5"/>
  <text x="110" y="666" font-family="Open Sans, sans-serif" font-size="38" fill="#111">$</text>
  <g font-family="Open Sans, sans-serif" font-size="19" fill="#fff">
    <text x="206" y="703">PHASE 1</text>
    <text x="385" y="647">PHASE 2</text>
    <text x="541" y="564">PHASE 3</text>
  </g>
</svg>

<section class="phase-table">
  <div class="cell head"><span class="phase-number">PHASE 1</span><span class="phase-name">Starting out</span></div>
  <div class="cell head"><span class="phase-number">PHASE 2</span><span class="phase-name">Laying the foundation</span></div>
  <div class="cell head"><span class="phase-number">PHASE 3</span><span class="phase-name">Break free</span></div>

  <div class="cell situation">
    <span class="cell-title">Your situation</span>
    <ul><li>Work full time</li><li>Eliminate debt</li><li>Save for first property</li><li>Consider other investments and savings plans</li></ul>
  </div>
  <div class="cell situation" style="justify-content:flex-start;padding-top:10px">
    <span class="cell-title">Your situation</span>
    <ul><li>Purchased first home</li><li>Start a family</li><li>Protect assets</li><li>Build investment portfolio</li><li>Start planning for the future</li><li>Implement correct tax structures</li></ul>
  </div>
  <div class="cell situation" style="justify-content:flex-start;padding-top:24px">
    <span class="cell-title">Your situation</span>
    <ul><li>Pay off your residential home</li><li>Purchase investment properties</li><li>Grow investment portfolio</li><li>Plan for retirement</li></ul>
  </div>

  <div class="cell">
    <span class="cell-title">Professionals involved</span>
    <ul><li>Budget coach</li><li>Financial adviser</li><li>Accountant</li></ul>
  </div>
  <div class="cell">
    <span class="cell-title">Professionals involved</span>
    <ul><li>Budget coach</li><li>Financial adviser</li><li>Mortgage broker</li><li>Accountant</li><li>Conveyancer</li></ul>
  </div>
  <div class="cell">
    <span class="cell-title">Professionals involved:</span>
    <ul><li>Budget coach</li><li>Financial adviser</li><li>Mortgage broker</li><li>Accountant</li><li>Conveyancer</li><li>Lawyer</li></ul>
  </div>
</section>

</body>
</html>
```